依頼概要
■ 依頼の目的/概要

概要
ほのかぜクリニックに併設したルミナステップは
代替医療をメインとした施設。
クリニックが全面サポート!!

★ほのかぜクリニックのコンセプト

ウィークリーホリデイズ
“毎日がクリスマスのように楽しく過ごしたい”
(ほのかぜクリニックホームページ参照:http://www.honokaze-cl.example/

医療機関ではあるが、固い感じではなく
明るなる。楽しくなる。元気になる。ようなイメージのデザインが良い。

ロゴマーク提供

>施設内内容
・有酸素運動設備
・ナノバブル温浴
・心体改善

■ パンフレットデザインへの要望

基本的には、会社ホームページの事業概要などに掲載している情報を会社案内にして頂きたいと思っています。

雰囲気やカラーはクリスマスの魔法にかけられたというコンセプト
ロゴマークを参照いただいて、イメージを膨らませてください。

◆四つ折り観音開きパンフレット

パンフレット内容
・表紙・裏表紙

・イメージページ
・施設内案内図

・有酸素運動設備
・ナノバブル温浴
・心体改善
・PRICE
・院長挨拶
・スタッフ紹介
・MAP
・施設名・住所・定休日・営業時間・など一式

■デザインレイアウトサンプル
*あくまでもサンプルレイアウトですので、自由にご提案ください。
女性誌のような雑誌のような構成が良いです。

●表
-----------------------------------------------------
https://drawpad.example/diagrams/QmTkwp4Lx8sbNvRa-7C21E.png
●裏
https://drawpad.example/diagrams/WbyhTo2KdVxePqLm-51AF9.png

●イメージサンプル
http://img.hondana.example/mag/QT_kenko_P/201007/k01/_SWF_Window.html
http://img.hondana.example/mag/QT_kenko_P/201007/k04/_SWF_Window.html

■ パンフレットの情報

ページ:8ページ(A4+α:4つ折り観音開き)
394mm(97mm.100mm.100mm.97mm)×210mm

■ 納品ファイルの希望

イラストレーター形式もしくはフォトショップ形式

■ 進め方

弊社の希望するイメージに近い提案を1つ(場合によって複数)選択させて頂きます。希望に近づけるために、修正要望を個別にさせて頂くこともあります。コンペ方式のため、修正後に当選されない場合も、どうかご了承ください。

■ その他/注意点

選択させて頂いたデザインの著作権(財産権)等の扱いはBorvane利用規約に従い、弊社に譲渡をお願いします。フォントや画像素材などを利用する場合は上記利用用途に使用できることを確認し、第三者の知的財産権等に注意して下さい。
名刺などにもイメージが生かせると今後使い勝手が良いと思いますので、そのあたりを配慮いただけると助かります。
デザインレイアウトサンプルの裏がログイン画面になっていました。
申し訳ございません。

設定変更いたしましたので、レイアウトイメージがご確認いただけると思います。

また、フォトにのイメージは素材集のモノでかまいませんので、ご提案くださいませ。
■ 選んだ理由

素敵なデザインをありがとうございますw。
ロゴと同じく感性が合うとの事でした。

長くお時間が掛かりました。すみませんw。

■ 提案者全員へのお礼・コメント

少しだけ修正がございますが、お願いします。

```html
<!DOCTYPE html>
<html lang="ja">
<head>
<meta charset="utf-8">
<title>ほのかぜクリニック ルミナステップ パンフレット</title>
<link href="https://fonts.googleapis.com/css2?family=Shippori+Mincho:wght@400&family=Noto+Sans+JP:wght@400;700;900&family=Montserrat:wght@700&display=swap" rel="stylesheet">
<style>
:root{
  --pink-top:#f4b5c2;
  --pink-mid:#ee9fb1;
  --pink-soft:#f8dbe2;
  --brand-red:#d9364f;
  --ink:#5a4a4e;
  --white:#ffffff;
  --cream:#efe6da;
}
*{margin:0;padding:0;box-sizing:border-box}
html,body{width:1200px;height:640px;overflow:hidden;background:#fff}
body{font-family:"Noto Sans JP",sans-serif;color:var(--ink)}
.spread{position:relative;width:1200px;height:640px;overflow:hidden}
.panel{position:absolute;top:0;height:640px;overflow:hidden}
.panel--inside-flap{left:0;width:298px}
.panel--staff{left:298px;width:302px;background:linear-gradient(180deg,var(--pink-top) 0%,var(--pink-mid) 45%,var(--pink-soft) 78%,#fdf3f5 100%)}
.panel--cover{left:600px;width:303px}
.panel--concept{left:903px;width:297px}

.photo{position:absolute;inset:0}
.photo--jewel{background:radial-gradient(ellipse at 40% 45%,#5a6e3e 0%,#8a7a55 25%,#cfc4b0 55%,var(--cream) 80%,#f5f1ea 100%)}
.photo--people{background:linear-gradient(180deg,#d7c9c9 0%,#e9c5cc 30%,#eaa9b8 60%,var(--pink-mid) 100%)}
.photo--tree{background:radial-gradient(ellipse at 40% 30%,#4a4c45 0%,#7b7a70 28%,#c9c3b8 55%,#e8e3dc 80%,#f1eee9 100%)}
.illust-staff{position:absolute;left:56px;top:180px;width:76px;height:66px;border-radius:6px;background:linear-gradient(180deg,#e7ecf2,#c8d2de)}

.flap-copy{position:absolute;right:4px;top:48px;height:262px;writing-mode:vertical-rl;font-size:8.2px;line-height:1.6;color:var(--ink)}
.flap-copy strong{display:block;font-size:10.5px;font-weight:700;margin-left:5px;white-space:nowrap}
.flap-copy small{display:block;font-size:7px;opacity:.8;margin-right:4px;font-family:"Montserrat",sans-serif}

.word-fragment{position:absolute;font-family:"Montserrat",sans-serif;font-weight:700;color:var(--white);letter-spacing:10px;font-size:13px}
.word-fragment--flap{left:8px;top:264px}

.closing-line{position:absolute;font-family:"Shippori Mincho",serif;color:var(--white);line-height:54px;white-space:nowrap;text-shadow:0 0 6px rgba(120,100,90,.25)}
.closing-line--flap{left:4px;top:528px;font-size:42px}
.closing-line--concept{left:14px;top:470px;font-size:46px}

/* staff */
.staff-title{position:absolute;left:66px;top:40px;display:flex;align-items:center;gap:8px;color:var(--white);font-weight:700;font-size:13px;letter-spacing:3px}
.staff-title svg{width:22px;height:22px}
.staff-list{position:absolute;left:24px;top:78px;width:270px;list-style:none}
.staff-row{display:flex;align-items:center;height:69px}
.role{flex:0 0 48px;height:48px;border-radius:50%;background:rgba(255,255,255,.25);border:1px solid rgba(255,255,255,.55);display:flex;align-items:center;justify-content:center;text-align:center;color:var(--white);font-size:9px;font-weight:700;line-height:1.25;margin-right:12px}
.role-text{font-size:7.4px;line-height:1.75;color:rgba(255,255,255,.95);white-space:nowrap}
.map{position:absolute;left:44px;top:426px;width:222px;height:108px;background:linear-gradient(180deg,#ffffff,#f6eef0);border:1px solid #d9c9cd}
.contact{position:absolute;left:10px;top:550px;width:290px;font-size:7.5px;line-height:1.5;color:var(--ink)}
.brand{position:absolute;left:0;top:4px;width:72px;text-align:center;color:var(--brand-red);font-weight:700;font-size:7px;line-height:1.35;white-space:nowrap}
.brand-mark{display:block;width:30px;height:30px;margin:0 auto 4px;border-radius:50%;background:var(--brand-red)}
.dial{position:absolute;left:78px;top:4px;display:flex;align-items:center;gap:6px}
.dial-label{font-size:6.5px;line-height:1.3;text-align:center}
.dial-number{font-size:17px;font-weight:700;letter-spacing:.5px;display:flex;align-items:center;gap:4px;white-space:nowrap}
.dial-number svg{width:18px;height:12px}
.hours{position:absolute;left:110px;top:28px;font-size:9px;font-weight:700;white-space:nowrap}
.hours small{font-size:6px;font-weight:400}
.address{position:absolute;left:78px;top:44px;font-size:6.2px;line-height:1.6;white-space:nowrap}

/* cover */
.headline{position:absolute;right:150px;top:174px;writing-mode:vertical-rl;color:var(--white);font-weight:900;font-size:20px;line-height:28px;letter-spacing:1px;white-space:nowrap}
.subcopy{position:absolute;right:204px;top:186px;writing-mode:vertical-rl;color:var(--white);font-size:10px;line-height:17px;font-weight:700;white-space:nowrap}
.cover-brand{position:absolute;left:0;top:524px;width:100%;text-align:center;color:var(--brand-red);font-weight:700;font-size:12px;line-height:1.4}
.cover-brand .brand-mark{width:48px;height:48px;margin-bottom:6px}

/* concept */
.concept-title{position:absolute;left:40px;top:242px;font-family:"Montserrat",sans-serif;font-weight:700;color:var(--white);font-size:13px;letter-spacing:12px;line-height:22px;white-space:nowrap}
.concept-sub{position:absolute;left:26px;top:288px;color:var(--white);font-weight:700;font-size:10.5px;white-space:nowrap}
</style>
</head>
<body>
<main class="spread">

  <section class="panel panel--inside-flap">
    <div class="photo photo--jewel" role="img" aria-label="宝石箱とネックレスの写真"></div>
    <div class="illust-staff" role="img" aria-label="クリニックのスタッフのイラスト"></div>
    <p class="flap-copy">
      <strong>「ウィークリーホリデイズ」が私たちの合い言葉</strong>
      「ウィークリーホリデイズ」の言葉には「毎日が楽しい」という意味があります。いつもあなたのそばに寄り添い健康をお届けしたいという想いを込めて、ほのかぜクリニックは笑顔あふれるスタッフがお待ちしています。
      <small>WeeklyHolidays</small>
    </p>
    <span class="word-fragment word-fragment--flap">YS</span>
    <p class="closing-line closing-line--flap">楽しい<br>指しています。</p>
  </section>

  <section class="panel panel--staff">
    <h2 class="staff-title">
      <svg viewBox="0 0 22 22" aria-hidden="true"><path d="M11 3c-4 0-6 3-6 7v4l-2 3h16l-2-3v-4c0-4-2-7-6-7z" fill="#f2c230"/><circle cx="11" cy="19" r="2" fill="#f2c230"/><path d="M8 3l3 2 3-2" stroke="#d9364f" stroke-width="2" fill="none"/></svg>
      スタッフ紹介
    </h2>
    <ul class="staff-list">
      <li class="staff-row"><span class="role">医師</span><p class="role-text">患者さま一人ひとりの声に耳を傾け、<br>からだと心の両面から丁寧に診療し、<br>笑顔で過ごせる毎日をサポートします。</p></li>
      <li class="staff-row"><span class="role">看護師</span><p class="role-text">やさしい声かけと細やかな気配りで、<br>安心して通っていただける環境を<br>スタッフ全員でつくっています。</p></li>
      <li class="staff-row"><span class="role">臨床工学<br>技士</span><p class="role-text">医療機器の管理と点検を毎日行い、<br>安全で快適な治療を支えています。<br>どんなことでもご相談ください。</p></li>
      <li class="staff-row"><span class="role">事 務<br>受 付</span><p class="role-text">明るい笑顔でお迎えいたします。<br>ご予約やお手続きのことなど、<br>お気軽にお声がけください。</p></li>
      <li class="staff-row"><span class="role">栄養士</span><p class="role-text">毎日の食事から健康づくりを考え、<br>無理なく続けられる食生活を<br>一緒に見つけていきましょう。</p></li>
    </ul>
    <div class="map" role="img" aria-label="クリニック周辺の道路と駅を示した案内地図"></div>
    <div class="contact">
      <div class="brand"><span class="brand-mark"></span>ほのかぜクリニック。<br>るみなすてっぷ</div>
      <div class="dial">
        <span class="dial-label">予約専用<br>フリーダイヤル</span>
        <span class="dial-number"><svg viewBox="0 0 18 12" aria-hidden="true"><rect x="0.5" y="0.5" width="17" height="11" rx="2" fill="none" stroke="#5a4a4e"/><circle cx="6" cy="6" r="2.6" fill="none" stroke="#5a4a4e"/><circle cx="12" cy="6" r="2.6" fill="none" stroke="#5a4a4e"/></svg>0120-480-316</span>
      </div>
      <p class="hours">open 10:00〜18:00 <small>定休日／日曜日・祝日</small></p>
      <p class="address">〒720-0000 広島県みどり市はるか町北1-23<br>TEL(084)000-1234　FAX(084)000-5678<br>URL www.honokaze-cl.example　Mail info@honokaze-cl.example</p>
    </div>
  </section>

  <section class="panel panel--cover">
    <div class="photo photo--people" role="img" aria-label="笑顔で語り合う男女の写真"></div>
    <h1 class="headline">からだの元気を<br>ドクターが徹底サポート</h1>
    <p class="subcopy">ほのかぜクリニックに併設したルミナステップは<br>代替医療をメインとした施設です。<br>クリニックが全面サポートしています!!</p>
    <div class="cover-brand"><span class="brand-mark"></span>ほのかぜクリニック。<br>るみなすてっぷ</div>
  </section>

  <section class="panel panel--concept">
    <div class="photo photo--tree" role="img" aria-label="小さなクリスマスツリーとハートの指輪の写真"></div>
    <p class="concept-title">WEEKLY<br>HOLIDA</p>
    <p class="concept-sub">“毎日がクリスマスのように楽しく過ごしたい”</p>
    <p class="closing-line closing-line--concept">私たちは、<br>いつも明るく<br>医療環境を目</p>
  </section>

</main>
</body>
</html>
```